Postcard Design

I want a postcard that I can use to advertise my farm.. I want to send it out to all the professional photographers within 100 miles.. hoping they will come for photo shoots. Also, eventually I will use this to advertise private events and parties here.. I want to be able to mail this out and have a collage of pictures, as well as the statement below
OAK HOLLER FARM- Celebrating country life!
contact: birdsong4821@mailnest.com or 205-478-2946

```html
<!DOCTYPE html>
<html lang="en">
<head>
<meta charset="utf-8">
<title>Oak Holler Farm Postcard</title>
<link href="https://fonts.googleapis.com/css2?family=Almendra+SC&family=Great+Vibes&family=Arimo:wght@400;700&display=swap" rel="stylesheet">
<style>
  :root {
    --page: #ece6dd;
    --forest: #3b4a24;
    --cream: #f4f1e6;
    --card: #ffffff;
    --gold-light: #d8c9a0;
    --gold-dark: #8c7547;
    --ink: #111111;
    --rule: #9a9a9a;
    --edge: #d9b99a;
  }
  * { box-sizing: border-box; margin: 0; padding: 0; }
  html, body { width: 991px; height: 1200px; overflow: hidden; }
  body { background: var(--page); position: relative; font-family: "Arimo", Arial, sans-serif; }

  .card { position: absolute; background: var(--card); }
  .front { left: 38px; top: 48px; width: 828px; height: 535px; }
  .back { left: 134px; top: 633px; width: 827px; height: 537px; }

  .masthead {
    position: absolute; background: var(--forest);
    display: flex; align-items: center; color: var(--cream);
  }
  .front .masthead { left: 0; top: 0; width: 828px; height: 112px; padding-left: 28px; }
  .back .masthead { left: 0; top: 0; width: 459px; height: 73px; padding-left: 30px; }

  .brand { display: flex; align-items: center; gap: 12px; }
  .brand-dot { border-radius: 50%; background: var(--cream); flex: none; }
  .front .brand-dot { width: 30px; height: 30px; }
  .back .brand-dot { width: 30px; height: 30px; }
  .brand-name { font-family: "Almendra SC", Georgia, serif; letter-spacing: 0.5px; white-space: nowrap; }
  .front .brand-name { font-size: 26px; }
  .back .brand-name { font-size: 27px; }

  .tagline {
    font-family: "Great Vibes", cursive; font-size: 44px;
    margin-left: 22px; white-space: nowrap;
  }

  .photo { position: absolute; }

  .contact-band {
    position: absolute; left: 0; top: 482px; width: 828px; height: 53px;
    background: linear-gradient(to bottom, var(--gold-light), var(--gold-dark));
    display: flex; align-items: center; justify-content: center;
    color: #fff; font-size: 15px; gap: 8px;
  }
  .contact-band svg { width: 16px; height: 16px; }
  .divider { margin: 0 8px; }

  .feature-panel {
    position: absolute; left: 0; top: 0; width: 459px; height: 410px;
    border-right: 1px solid var(--edge); border-bottom: 1px solid var(--edge);
    border-bottom-right-radius: 10px;
  }
  .invite {
    position: absolute; left: 0; top: 332px; width: 459px;
    text-align: center; font-size: 15px; line-height: 19.5px; color: var(--ink);
  }
  .phone-pill {
    position: absolute; left: 66px; top: 411px; width: 327px; height: 34px;
    background: linear-gradient(to bottom, var(--gold-light), var(--gold-dark));
    border-radius: 0 0 12px 12px;
    display: flex; align-items: center; justify-content: center; gap: 8px;
    color: #fff; font-weight: 700; font-size: 20px;
  }
  .phone-pill svg { width: 20px; height: 20px; }

  .stamp-box { position: absolute; left: 700px; top: 39px; width: 104px; height: 84px; border: 1px solid var(--rule); }
  .address-line { position: absolute; left: 550px; width: 254px; height: 0; border-top: 1px solid var(--rule); }

  .foot-band {
    position: absolute; left: 0; top: 515px; width: 827px; height: 22px;
    background: linear-gradient(to bottom, var(--gold-light), var(--gold-dark));
  }
</style>
</head>
<body>

<section class="card front">
  <header class="masthead">
    <div class="brand">
      <span class="brand-dot"></span>
      <span class="brand-name">OAK HOLLER FARM</span>
    </div>
    <span class="tagline">Celebrating country life!</span>
  </header>

  <div class="photo" role="img" aria-label="Tree-lined drive opening onto a sunny pasture with fencing" style="left:14px;top:129px;width:397px;height:330px;background:linear-gradient(to bottom,#a9cdea 0%,#5d7b3c 45%,#6f8a3a 70%,#6b5440 100%);"></div>
  <div class="photo" role="img" aria-label="Stacked stone wall with ferns in clay pots" style="left:417px;top:129px;width:196px;height:161px;background:linear-gradient(to bottom,#6e8a48,#6c655a 40%,#5d574d);"></div>
  <div class="photo" role="img" aria-label="Pool house beside a blue swimming pool" style="left:618px;top:129px;width:196px;height:161px;background:linear-gradient(to bottom,#b5cf8a,#c9c3b0 45%,#3fa4d4 75%,#4fb6e0);"></div>
  <div class="photo" role="img" aria-label="Mule looking over a wooden fence with a barn behind" style="left:417px;top:298px;width:196px;height:161px;background:linear-gradient(to bottom,#a7c27a,#b58558 50%,#7a6a55);"></div>
  <div class="photo" role="img" aria-label="Old wagon wheel leaning against a tree on green lawn" style="left:618px;top:298px;width:196px;height:161px;background:linear-gradient(to bottom,#a9c58c,#4e5a32 45%,#5f9a45);"></div>

  <footer class="contact-band">
    <span>Please contact us on:</span>
    <svg viewBox="0 0 20 20" aria-hidden="true"><circle cx="10" cy="10" r="8.8" fill="none" stroke="#fff" stroke-width="1.6"/><path d="M7 5.5l1.6 2.3-1 1.2c.6 1.3 1.6 2.3 2.9 2.9l1.2-1 2.3 1.6-.9 1.6c-3.6-.3-6.6-3.3-6.9-6.9z" fill="#fff"/></svg>
    <span>205-478-2946</span>
    <span class="divider">|</span>
    <svg viewBox="0 0 20 20" aria-hidden="true"><path d="M2 9l8-6 8 6v8H2z" fill="#fff"/><path d="M2 9l8 5 8-5" fill="none" stroke="#a08a5a" stroke-width="1.4"/></svg>
    <span>birdsong4821@mailnest.com</span>
  </footer>
</section>

<section class="card back">
  <div class="feature-panel">
    <header class="masthead">
      <div class="brand">
        <span class="brand-dot"></span>
        <span class="brand-name">OAK HOLLER FARM</span>
      </div>
    </header>

    <div class="photo" role="img" aria-label="Farm entrance sign on dark posts at dusk" style="left:0;top:96px;width:162px;height:216px;background:linear-gradient(to bottom,#b8d3e8,#8fa7b5 40%,#2b2e25 55%,#7a5a3e);"></div>
    <div class="photo" role="img" aria-label="Wide pasture with shade trees and black fencing" style="left:174px;top:96px;width:285px;height:103px;background:linear-gradient(to bottom,#a4c7e6,#4f6d35 40%,#3a3d2b 65%,#6fa24a);"></div>
    <div class="photo" role="img" aria-label="Garden lamp post and flower bed by the lawn" style="left:174px;top:205px;width:141px;height:107px;background:linear-gradient(to bottom,#9ec07a,#55763a 50%,#6c8f45);"></div>
    <div class="photo" role="img" aria-label="Metal horse silhouettes set beneath a tree" style="left:321px;top:205px;width:138px;height:107px;background:linear-gradient(to bottom,#7a9a55,#6b5a45 55%,#8a6f55);"></div>

    <p class="invite">Enjoy the beautiful setting of this unique property<br>and let us create an unforgettable experience<br>for your special occasion.</p>
  </div>

  <div class="phone-pill">
    <svg viewBox="0 0 20 20" aria-hidden="true"><circle cx="10" cy="10" r="8.8" fill="none" stroke="#fff" stroke-width="1.6"/><path d="M7 5.5l1.6 2.3-1 1.2c.6 1.3 1.6 2.3 2.9 2.9l1.2-1 2.3 1.6-.9 1.6c-3.6-.3-6.6-3.3-6.9-6.9z" fill="#fff"/></svg>
    <span>205-478-2946</span>
  </div>

  <div class="stamp-box"></div>
  <div class="address-line" style="top:231px"></div>
  <div class="address-line" style="top:270px"></div>
  <div class="address-line" style="top:309px"></div>
  <div class="address-line" style="top:348px"></div>

  <div class="foot-band"></div>
</section>

</body>
</html>
```